Clean invitation for a wedding

Design a wedding invitation.
Those examples in attachment. They are looking for this style, about the same construction. Back with the symbols etc.

Clean sleek design.

marriage name:
Kemp & Rosetta
02.06.23

You can copy the rest of the texts from the examples.

```html
<!DOCTYPE html>
<html lang="en">
<head>
<meta charset="utf-8">
<title>Kemp &amp; Rosetta – Wedding Invitation</title>
<link href="https://fonts.googleapis.com/css2?family=Mrs+Saint+Delafield&family=Jost:wght@400;600&family=Bodoni+Moda:wght@700&display=swap" rel="stylesheet">
<style>
  :root{
    --bg:#ecebe8;
    --paper:#f1ece2;
    --ink:#141414;
  }
  html,body{margin:0;padding:0;overflow:hidden;}
  body{width:1200px;height:1200px;background:var(--bg);position:relative;font-family:'Jost',sans-serif;color:var(--ink);}
  .card{position:absolute;top:194px;width:540px;height:812px;background:var(--paper);box-shadow:0 2px 10px rgba(0,0,0,.06);}
  .card--invite{left:40px;}
  .card--program{left:620px;}
  .abs{position:absolute;left:0;right:0;text-align:center;}
  .caps{text-transform:uppercase;letter-spacing:.2em;font-size:11px;line-height:15px;}
  .script{font-family:'Mrs Saint Delafield',cursive;font-weight:400;}
  .invite__intro{top:52px;}
  .couple{position:absolute;left:0;top:100px;width:540px;height:290px;transform:rotate(-5deg);}
  .couple__line{position:absolute;font-family:'Mrs Saint Delafield',cursive;font-size:150px;line-height:1;white-space:nowrap;}
  .couple__first{left:80px;top:10px;}
  .couple__second{left:110px;top:120px;}
  .invite__date{top:500px;font-family:'Bodoni Moda',serif;font-weight:700;font-size:46px;letter-spacing:.12em;}
  .invite__time{top:554px;font-size:12px;}
  .invite__venue{top:598px;font-weight:600;font-size:12px;}
  .invite__city{top:614px;font-size:8.5px;letter-spacing:.18em;}
  .invite__rsvp-title{top:660px;font-size:48px;line-height:1;}
  .invite__rsvp-line{top:728px;font-size:11.5px;}
  .invite__rsvp-mail{top:744px;font-size:11.5px;}
  .program__title{top:52px;font-size:70px;line-height:1;}
  .timeline{position:absolute;left:269px;top:171px;width:1.5px;height:560px;background:var(--ink);}
  .dot{position:absolute;left:267px;width:5px;height:5px;border-radius:50%;background:var(--ink);}
  .event{position:absolute;left:300px;width:180px;text-align:center;}
  .event__time{font-size:11px;letter-spacing:.25em;}
  .event__name{font-size:11px;letter-spacing:.22em;text-transform:uppercase;margin-top:16px;}
  .icon{position:absolute;left:133px;width:40px;height:40px;}
  .icon svg{width:40px;height:40px;fill:none;stroke:var(--ink);stroke-width:1.6;stroke-linecap:round;stroke-linejoin:round;}
  .icon--placeholder{background:linear-gradient(#e3ddd1,#d6cfc2);border-radius:50%;}
</style>
</head>
<body>

<section class="card card--invite">
  <p class="abs caps invite__intro" style="margin:0">Please join us to<br>celebrate the wedding of</p>
  <div class="couple">
    <span class="couple__line couple__first">Kemp &amp;</span>
    <span class="couple__line couple__second">Rosetta</span>
  </div>
  <div class="abs invite__date">02.06.23</div>
  <div class="abs caps invite__time">10' clock in the afternoon</div>
  <div class="abs caps invite__venue">At Cedar Hollow Estate</div>
  <div class="abs caps invite__city">Malibu, California</div>
  <div class="abs script invite__rsvp-title">RVSP</div>
  <div class="abs caps invite__rsvp-line">Kindly RVSP to Kemp by April 30th 2022</div>
  <div class="abs caps invite__rsvp-mail">kempandrosettawedding@ourmail.example</div>
</section>

<section class="card card--program">
  <div class="abs script program__title">Program</div>
  <div class="timeline"></div>

  <!-- Wedding -->
  <div class="icon" style="top:174px">
    <svg viewBox="0 0 40 40"><circle cx="15" cy="24" r="9"/><circle cx="25" cy="24" r="9"/><path d="M11 12l4-5 4 5-4 3z"/></svg>
  </div>
  <div class="dot" style="top:206px"></div>
  <div class="event" style="top:170px"><div class="event__time">13.30</div><div class="event__name">Wedding</div></div>

  <!-- Relaxation -->
  <div class="icon" style="top:282px">
    <svg viewBox="0 0 40 40"><path d="M8 12l8 3-2 8-7-3z"/><path d="M32 12l-8 3 2 8 7-3z"/><path d="M10 21l-2 10M30 21l2 10M5 31h6M29 31h6"/><path d="M18 6l2 3 2-3"/></svg>
  </div>
  <div class="dot" style="top:314px"></div>
  <div class="event" style="top:278px"><div class="event__time">15.00</div><div class="event__name">Relaxation and fun</div></div>

  <!-- Cake -->
  <div class="icon" style="top:390px">
    <svg viewBox="0 0 40 40"><rect x="14" y="10" width="12" height="7"/><rect x="11" y="17" width="18" height="7"/><rect x="8" y="24" width="24" height="7"/><path d="M6 34h28M20 34v3M15 37h10M20 6v4"/></svg>
  </div>
  <div class="dot" style="top:422px"></div>
  <div class="event" style="top:386px"><div class="event__time">16.00</div><div class="event__name">Wedding cake</div></div>

  <!-- Lunch -->
  <div class="icon" style="top:498px">
    <svg viewBox="0 0 40 40"><circle cx="20" cy="20" r="9"/><circle cx="20" cy="20" r="5.5"/><path d="M5 6v10M3 6v6a2 2 0 004 0V6M5 16v18M35 6c-3 3-3 9 0 11v17"/></svg>
  </div>
  <div class="dot" style="top:530px"></div>
  <div class="event" style="top:494px"><div class="event__time">17.30</div><div class="event__name">Lunch</div></div>

  <!-- First dance -->
  <div class="icon icon--placeholder" style="top:606px" role="img" aria-label="Small line icon of a couple sharing their first dance"></div>
  <div class="dot" style="top:638px"></div>
  <div class="event" style="top:602px"><div class="event__time">23.00</div><div class="event__name">Wedding first dance</div></div>

  <!-- Party -->
  <div class="icon" style="top:714px">
    <svg viewBox="0 0 40 40"><circle cx="20" cy="20" r="12"/><circle cx="20" cy="20" r="7"/><path d="M18 23v-5l4-1v5"/><circle cx="17" cy="23" r="1"/><circle cx="21" cy="22" r="1"/><path d="M6 14a15 15 0 000 12M34 14a15 15 0 010 12M8 5l1 2M33 5l-1 2"/></svg>
  </div>
  <div class="dot" style="top:746px"></div>
  <div class="event" style="top:710px"><div class="event__time">00.00</div><div class="event__name">Party</div></div>
</section>

</body>
</html>
```